Camp Brambleton Day Camp Brochure

I need someone to design a brochure for our day camp. It will be 8.5 x 11 inch paper folded horizontally. Looking for a fun, clean design. I sent several pictures, not all of them have to be used. The brochure will be mailed out to former day campers and used at events to help us market our program. A colorful brochure would be nice. I would like the cover page to be portrait along with the two inside pages. The back cover will need to be landscape format.

Target Market(s)

Parents

Colors

Designer to choose colors to be used in the design.

Requirements
Must have
• All information provided. Great design on the inside pages

```html
<!DOCTYPE html>
<html lang="en">
<head>
<meta charset="utf-8">
<title>Camp Brambleton Day Camp 2019 Brochure</title>
<link href="https://fonts.googleapis.com/css2?family=Montserrat:ital,wght@0,400;0,500;0,600;0,700;0,800;1,600&display=swap" rel="stylesheet">
<style>
:root{
  --bg:#2f2f2f;
  --green:#2f7d1f;
  --green-dark:#236415;
  --red:#7d1510;
  --red-deep:#560b07;
  --white:#ffffff;
  --ink:#222222;
  --charcoal:#333333;
  --muted:#555555;
}
*{box-sizing:border-box;margin:0;padding:0}
html,body{width:840px;height:1200px;overflow:hidden;background:var(--bg);font-family:'Montserrat',sans-serif;color:var(--ink)}
.spread{position:absolute;left:50px;width:740px;height:572px;display:flex;box-shadow:0 8px 24px rgba(0,0,0,.45)}
.spread--outside{top:18px}
.spread--inside{top:610px}
.page{position:relative;width:370px;height:572px;overflow:hidden;background:var(--white)}

/* back cover */
.mail-strip{position:absolute;left:0;top:0;width:112px;height:572px;background:var(--white)}
.return-address{position:absolute;left:20px;bottom:24px;transform:rotate(-90deg);transform-origin:left bottom;width:260px;translate:100% 0;left:0;font-size:7px;line-height:1.45;color:var(--ink)}
.return-address strong{display:block;font-size:12px;font-weight:700;letter-spacing:.5px;margin-bottom:6px}
.resident{position:absolute;left:72px;top:120px;transform:rotate(-90deg);transform-origin:left top;font-size:6px;letter-spacing:.3px;white-space:nowrap}
.postage{position:absolute;left:70px;top:18px;width:30px;height:44px;border:1px solid #ccc;font-size:4px;line-height:1.3;padding:2px;color:var(--muted);writing-mode:vertical-rl;transform:rotate(180deg)}
.photo{position:absolute}
.back-photo{left:112px;top:0;width:258px;height:500px;background:linear-gradient(160deg,#6f8f4c 0%,#a9b98a 40%,#8a8478 70%,#c8c2b8 100%)}
.band{position:absolute;left:0;bottom:0;width:100%;height:72px;background:var(--green);color:var(--white);font-size:9px;font-weight:500;display:flex;align-items:center;justify-content:center;gap:6px}
.back-band{left:112px;width:258px}
.globe{width:9px;height:9px}

/* cover */
.cover-photo{left:0;top:0;width:370px;height:500px;background:linear-gradient(170deg,#4e7a3a 0%,#8fb06a 35%,#c9b79a 65%,#a88e6e 100%)}
.cover-title{position:absolute;left:60px;top:312px;width:260px;padding:12px 18px;background:rgba(40,40,40,.85);color:var(--white)}
.cover-title span{display:block;font-size:17px;font-weight:500}
.cover-title b{display:block;font-size:25px;font-weight:700;line-height:1.1}
.cover-accent{position:absolute;left:40px;top:378px;width:50px;height:5px;background:var(--green)}

/* inside */
.red-field{position:absolute;left:0;top:0;width:100%;height:100%;background:radial-gradient(ellipse at 80% 30%,var(--red) 0%,var(--red-deep) 100%)}
.content{position:absolute;left:26px;right:22px;color:var(--white)}
.intro{top:26px;font-size:8.6px;line-height:1.35}
.intro h2{font-size:14px;font-weight:800;font-style:italic;display:inline}
.intro .lead{font-weight:700;font-style:italic;font-size:10px;margin-bottom:8px}
.intro p{margin-bottom:8px}
.intro .age{font-weight:700;font-style:italic;font-size:9.5px}
.price-row{display:flex;gap:6px;margin-bottom:4px}
.price-label{background:var(--green);width:140px;padding:3px 10px;font-weight:700;font-size:9px;letter-spacing:.4px}
.price-value{background:var(--white);color:var(--red);width:62px;text-align:center;padding:3px 0;font-weight:700;font-size:9.5px}
.bus-note{font-size:6.3px;line-height:1.4;margin-top:6px}
.camp-photos{left:26px;top:350px;width:318px;height:170px}
.group-photo-1{left:0;top:0;width:318px;height:84px;background:linear-gradient(90deg,#5a6a44,#9aa07a,#6f7b52)}
.group-photo-2{left:0;top:86px;width:318px;height:84px;background:linear-gradient(90deg,#8a5a48,#c79a88,#7a4d3c)}
.bottom-curve{position:absolute;left:0;bottom:0;width:370px;height:120px}

.right-content{left:26px;right:26px}
.section-title{font-size:14px;font-weight:800;margin-bottom:2px}
.title-rule{width:22px;height:4px;border-radius:2px;background:var(--green);margin-bottom:8px}
.bus{top:48px}
.stop{display:flex;align-items:center;gap:6px;margin-bottom:3px}
.stop-name{flex:1;border:1px solid rgba(255,255,255,.6);border-radius:3px;padding:2px 8px;font-size:7.5px;font-weight:600}
.stop-time{background:var(--green);width:110px;border-radius:3px;padding:2px 0;text-align:center;font-size:8px;font-weight:700}
.discounts{top:160px;font-size:6.8px;line-height:1.45}
.discounts em{font-style:normal;font-weight:700;color:#5fc24a}
.weeks{top:262px}
.week-grid{display:grid;grid-template-columns:1fr 1fr;column-gap:12px;row-gap:4px}
.week{display:flex;gap:4px;align-items:center}
.week-label{width:46px;border:1px solid rgba(255,255,255,.6);border-radius:3px;padding:2px 4px;font-size:7px;font-weight:700}
.week-dates{flex:1;background:var(--white);color:var(--ink);border-radius:3px;padding:2px 6px;font-size:7.5px;font-weight:700;text-align:center}
.register{position:absolute;left:0;right:0;bottom:0;height:110px;background:var(--white);text-align:center;padding-top:14px}
.register small{display:block;font-size:9px;font-weight:600;color:var(--charcoal)}
.register-pill{display:inline-block;margin:6px 0;background:var(--green);color:var(--white);border-radius:16px;padding:6px 44px;font-size:15px;font-weight:800}
.register-rule{position:absolute;left:0;bottom:0;width:100%;height:6px;background:var(--green)}
</style>
</head>
<body>

<section class="spread spread--outside">
  <div class="page page--back">
    <div class="mail-strip">
      <div class="postage">Nonprofit Org US Postage Paid Permit 00</div>
      <div class="resident">OR CURRENT RESIDENT</div>
      <div class="return-address"><strong>CAMP BRAMBLETON</strong>PO Box 4410<br>Millbrook, AR<br>555-010-3000<br>office@campbrambleton.org</div>
    </div>
    <div class="photo back-photo" role="img" aria-label="Photo of a smiling child eating a slice of watermelon outdoors"></div>
    <div class="band back-band">
      <svg class="globe" viewBox="0 0 10 10"><circle cx="5" cy="5" r="4.3" fill="none" stroke="#fff" stroke-width="1"/><path d="M1 5h8M5 .7c2 2.5 2 6 0 8.6M5 .7c-2 2.5-2 6 0 8.6" fill="none" stroke="#fff" stroke-width=".8"/></svg>
      www.campbrambleton.org
    </div>
  </div>

  <div class="page page--cover">
    <div class="photo cover-photo" role="img" aria-label="Photo of a child in a riding helmet on horseback, waving, in front of green trees"></div>
    <div class="cover-accent"></div>
    <div class="cover-title"><span>Camp Brambleton</span><b>Day Camp 2019</b></div>
    <div class="band">
      <svg class="globe" viewBox="0 0 10 10"><circle cx="5" cy="5" r="4.3" fill="none" stroke="#fff" stroke-width="1"/><path d="M1 5h8M5 .7c2 2.5 2 6 0 8.6M5 .7c-2 2.5-2 6 0 8.6" fill="none" stroke="#fff" stroke-width=".8"/></svg>
      www.campbrambleton.org
    </div>
  </div>
</section>

<section class="spread spread--inside">
  <div class="page page--inside-left">
    <div class="red-field"></div>
    <div class="content intro">
      <div class="lead"><h2>Since 1980,</h2> Camp Brambleton has offered day camp. This summer, we have nine one-week sessions. Come to one session or all nine.</div>
      <p>Each week our activities include swimming, horseback riding, Bible lessons, singing, arts and crafts, cookouts, hiking, and much more.</p>
      <p class="age">Day camp is open to all kids ages 5 and up. Costs are as follows for one session of day camp:</p>
      <div class="price-row"><div class="price-label">5-7 YEAR OLDS</div><div class="price-value">$105</div></div>
      <div class="price-row"><div class="price-label">8 YEARS AND UP</div><div class="price-value">$120</div></div>
      <p class="bus-note">For your convenience we run a bus in Millbrook each day to pick-up and drop-off campers. Please see the bus schedule below for locations and times. Campers may be dropped off and picked up between 7:45 a.m. and 4:45 p.m. at Brambleton if you prefer.</p>
    </div>
    <svg class="bottom-curve" viewBox="0 0 370 120" preserveAspectRatio="none">
      <path d="M0 48 H200 C260 48 290 40 370 0 V120 H0Z" fill="#fff"/>
      <path d="M0 112 H370 V120 H0Z" fill="#2f7d1f"/>
    </svg>
    <div class="photo camp-photos">
      <div class="photo group-photo-1" role="img" aria-label="Photo of a group of campers standing among trees"></div>
      <div class="photo group-photo-2" role="img" aria-label="Photo of campers sitting together on benches indoors"></div>
    </div>
  </div>

  <div class="page page--inside-right">
    <div class="red-field"></div>
    <div class="content right-content bus">
      <h3 class="section-title">Bus Stop Schedule</h3>
      <div class="title-rule"></div>
      <div class="stop"><span class="stop-name">First Community Chapel</span><span class="stop-time">7:15 a.m./5:30 p.m.</span></div>
      <div class="stop"><span class="stop-name">Hollis Center</span><span class="stop-time">7:30 a.m./5:15 p.m.</span></div>
      <div class="stop"><span class="stop-name">Main Street Church</span><span class="stop-time">7:45 a.m./5:00 p.m.</span></div>
    </div>
    <div class="content right-content discounts">
      <h3 class="section-title">Discounts</h3>
      <div class="title-rule"></div>
      <p><em>Early Bird:</em> A $5 discount per session, per child is offered if the child is registered by May 1st.</p>
      <p><em>Siblings:</em> $5 off per child for each session, per family.</p>
      <p><em>Multi-Session:</em> $5 off per child, per session if you register for more than one session.</p>
    </div>
    <div class="content right-content weeks">
      <h3 class="section-title">Weeks</h3>
      <div class="title-rule"></div>
      <div class="week-grid">
        <div class="week"><span class="week-label">Week 1:</span><span class="week-dates">June 3rd - 7th</span></div>
        <div class="week"><span class="week-label">Week 2:</span><span class="week-dates">June 10th - 14th</span></div>
        <div class="week"><span class="week-label">Week 3:</span><span class="week-dates">June 17th - 21st</span></div>
        <div class="week"><span class="week-label">Week 4:</span><span class="week-dates">June 24th - 28th</span></div>
        <div class="week"><span class="week-label">Week 5:</span><span class="week-dates">July 1st - 5th</span></div>
        <div class="week"><span class="week-label">Week 6:</span><span class="week-dates">July 8th - 12th</span></div>
        <div class="week"><span class="week-label">Week 7:</span><span class="week-dates">July 15th - 19th</span></div>
        <div class="week"><span class="week-label">Week 8:</span><span class="week-dates">July 22nd - 26th</span></div>
        <div class="week"><span class="week-label">Week 9:</span><span class="week-dates">July 29 - August 2nd</span></div>
      </div>
    </div>
    <div class="register">
      <small>Register today at</small>
      <div class="register-pill">campbrambleton.org!</div>
      <small>Spaces are limited</small>
      <div class="register-rule"></div>
    </div>
  </div>
</section>

</body>
</html>
```